KW Depot ltd*

I need a full website designed for for a 10,000m2 strorage facity which specialize in heavy commercial storage

it needs to be in english please

Target Market(s)

Comercial sector

Industry/Entity Type

Construction Company

Logo Text

KW

Coding

Coded - Design and coding required

Number of Pages Required

1 page

Font styles to use
Sans Serif

Colors
ec1f27
ffffff

Requirements
Must have
• Tel 0064 219486375
• email- mark@kwdepot.co.nz
Nice to have
• We specilize in large items with the facilty have 3 15tonne Gantry cranes and heavy mobile lifting equipment we can store items up to 20 tonne and we are fully covered and secure.
• square meter rates from 20m2 to 10,000 m2

```html
<!DOCTYPE html>
<html lang="en">
<head>
<meta charset="utf-8">
<title>KW Depot ltd – Heavy Commercial Storage</title>
<link href="https://fonts.googleapis.com/css2?family=Lato:wght@300;400;700;900&display=swap" rel="stylesheet">
<style>
:root{
  --red:#ec1f27;
  --red-dark:#c8161d;
  --white:#ffffff;
  --navy:#0d1b2e;
  --ink:#2b2b2b;
  --grey:#7a7a7a;
  --line:#d9d9d9;
  --teal:#4a8c8c;
  --dark-band:#262c33;
}
*{margin:0;padding:0;box-sizing:border-box}
html,body{width:1200px;height:4523px;overflow:hidden}
body{font-family:'Lato',sans-serif;color:var(--ink);background:var(--white);position:relative}
.abs{position:absolute}
.red{color:var(--red)}
.btn{position:absolute;background:var(--red);color:var(--white);font-size:9px;font-weight:700;text-transform:uppercase;display:flex;align-items:center;justify-content:center;border-radius:3px;letter-spacing:.3px}
.eyebrow{font-size:11px;text-transform:uppercase;color:var(--grey);letter-spacing:.3px}
.heading{font-weight:900;color:var(--red);text-transform:uppercase;letter-spacing:-.3px}
.rule{height:2px;background:var(--teal)}
.body-text{font-size:12px;line-height:16px;color:var(--grey)}

/* top bar */
.topbar{left:0;top:0;width:1200px;height:30px;background:var(--navy);color:#fff;font-size:8px;font-weight:700}
.topbar span{position:absolute;top:10px}
/* header */
.header{left:0;top:30px;width:1200px;height:181px;background:var(--white)}
.brand{left:84px;top:70px;display:flex;align-items:center;gap:10px}
.brand i{width:22px;height:22px;border-radius:50%;background:var(--red);display:block}
.brand b{font-size:30px;font-weight:900;color:var(--red);letter-spacing:.5px}
.contact-item{display:flex;align-items:center;gap:12px;color:#fff}
.contact-item .t1{font-size:27px;font-weight:400;line-height:27px}
.contact-item .t2{font-size:12px}
.quote-btn{left:966px;top:79px;width:104px;height:39px;background:#fff;color:var(--red);font-size:8px;display:flex;align-items:center;justify-content:center;border-radius:3px;text-transform:uppercase}
.nav{top:158px;left:386px;display:flex;gap:0;font-size:8px;color:#fff;font-weight:700;text-transform:uppercase}
.nav span{margin-right:36px}
/* hero */
.hero{left:0;top:211px;width:1200px;height:670px;background:linear-gradient(180deg,#0e2744 0%,#1f4f7f 45%,#3a6e9d 75%,#5e8fb8 100%)}
.hero h1{left:128px;top:112px;font-size:54px;line-height:62px;font-weight:400;color:#fff;text-transform:uppercase}
.hero .rule{left:128px;top:263px;width:140px}
.hero p{left:128px;top:282px;font-size:25px;color:#fff}
/* why */
.why{left:128px;top:682px;width:942px;height:530px;background:#fff;box-shadow:0 4px 18px rgba(0,0,0,.18)}
.feature{left:559px;width:260px}
.feature h4{font-size:12px;font-weight:700;color:#444;margin-bottom:6px}
.feature p{font-size:11.5px;line-height:16px;color:var(--grey)}
.feature svg{position:absolute;left:-67px;top:0}
/* services */
.svc-card{top:1440px;width:304px;height:417px;border:1px solid var(--line);background:#fff}
.svc-card .photo{width:100%;height:208px}
.svc-card h3{position:absolute;left:23px;top:238px;font-size:18px;font-weight:900;color:var(--red)}
.svc-card p{position:absolute;left:23px;top:284px;width:262px;font-size:11.5px;line-height:16px;color:var(--grey)}
.svc-card .btn{left:23px;top:355px;width:78px;height:24px}
/* about */
.about{left:0;top:2006px;width:1200px;height:626px;background:linear-gradient(180deg,#2c3238,#1e2329)}
.about-text{left:606px;color:#fff}
/* testimonial */
.testi{left:128px;top:2454px;width:942px;height:440px;background:#fff;box-shadow:0 4px 18px rgba(0,0,0,.15)}
/* goals */
.goal{left:128px;width:464px;height:197px;border:1px solid var(--line);background:#fff}
.goal h3{position:absolute;left:150px;top:30px;font-size:18px;font-weight:900;color:#555;text-transform:uppercase}
.goal p{position:absolute;left:150px;top:82px;width:280px;font-size:12px;line-height:16px;color:var(--grey)}
.goal svg{position:absolute;left:46px;top:28px}
.faq{left:687px;width:383px;height:44px;background:var(--red);color:#fff;font-size:14px;display:flex;align-items:center;justify-content:center;border-radius:2px}
.faq svg{position:absolute;right:20px;top:14px}
/* quote */
.quote-band{left:0;top:3623px;width:1200px;height:520px;background:linear-gradient(135deg,#3a1f24 0%,#2a2f3a 40%,#4b2226 70%,#1e2430 100%)}
.quote-box{left:329px;top:3690px;width:542px;height:386px;background:rgba(110,110,118,.78)}
.field{position:absolute;width:180px;height:42px;background:#fff;color:#aaa;font-size:11px;display:flex;align-items:center;justify-content:center}
/* footer */
.footer{left:0;top:4143px;width:1200px;height:380px;background:var(--red);color:#fff}
.footer h5{position:absolute;top:118px;font-size:17px;font-weight:900;text-transform:uppercase}
.footer ul{position:absolute;top:160px;list-style:none;font-size:13px}
.footer li{height:31px;display:flex;gap:10px;align-items:flex-start}
.footer li::before{content:"›";font-size:12px;line-height:14px}
</style>
</head>
<body>

<div class="abs topbar">
  <span style="left:804px">Opening Hours: Monday - Saturday 9Am To 5 pm</span>
  <span style="left:1021px;top:6px;height:18px;border-left:1px solid #55607a"></span>
  <span style="left:1032px">NZ</span>
</div>

<header class="abs header">
  <svg class="abs" style="left:0;top:0" width="1200" height="181"><polygon points="246,0 1200,0 1200,181 378,181" fill="#ec1f27"/><line x1="296" y1="137" x2="1200" y2="137" stroke="#c8161d" stroke-width="2"/></svg>
  <div class="abs brand"><i></i><b>KW DEPOT</b></div>
  <div class="abs contact-item" style="left:562px;top:43px">
    <svg width="40" height="40" viewBox="0 0 40 40" fill="none" stroke="#fff" stroke-width="2"><path d="M10 6l7 7-4 4c2 5 6 9 11 11l4-4 7 7-5 5C18 35 5 22 5 11z"/></svg>
    <div><div class="t1">Free Call</div><div class="t2">0064 219486375</div></div>
  </div>
  <div class="abs contact-item" style="left:755px;top:43px">
    <svg width="44" height="40" viewBox="0 0 44 40" fill="none" stroke="#fff" stroke-width="2"><rect x="3" y="10" width="38" height="26"/><path d="M3 10l19 15 19-15"/></svg>
    <div><div class="t1">Mail Us</div><div class="t2">mark@kwdepot.co.nz</div></div>
  </div>
  <div class="abs quote-btn">Get a quote</div>
  <nav class="abs nav"><span>Home ▾</span><span>About us</span><span>Service ▾</span><span>Blog</span><span>Pages ▾</span><span>Contact</span></nav>
  <svg class="abs" style="left:1040px;top:148px" width="20" height="20" fill="none" stroke="#fff" stroke-width="2"><circle cx="8" cy="8" r="6"/><path d="M13 13l6 6"/></svg>
</header>

<section class="abs hero" role="img" aria-label="Photo of a large warehouse interior with trucks and workers">
  <h1 class="abs">No# 1 Solution<br>for Warehouse</h1>
  <div class="abs rule"></div>
  <p class="abs">We Specialize in Heavy commercial storage</p>
  <div class="btn" style="left:128px;top:339px;width:104px;height:42px;font-size:8px">See services</div>
</section>

<section class="abs why">
  <svg class="abs" style="left:0;top:0" width="542" height="530" role="img" aria-label="Photo of stacked shipping containers with a plane overhead">
    <defs><linearGradient id="g1" x1="0" y1="0" x2="1" y2="1"><stop offset="0" stop-color="#9bb7d6"/><stop offset=".5" stop-color="#6f6f8a"/><stop offset="1" stop-color="#3a3f58"/></linearGradient></defs>
    <polygon points="0,0 472,0 542,530 0,530" fill="url(#g1)"/>
  </svg>
  <div class="abs eyebrow" style="left:559px;top:56px;font-size:9px">Features</div>
  <div class="abs heading" style="left:559px;top:70px;font-size:19px">Why choose us</div>
  <div class="abs" style="left:559px;top:103px;width:64px;height:2px;background:#999"></div>
  <div class="abs feature" style="top:159px">
    <svg width="44" height="44" fill="none" stroke="#ec1f27" stroke-width="1.6"><circle cx="20" cy="20" r="17"/><path d="M20 10v10l7 4"/><text x="24" y="40" font-size="13" fill="#ec1f27" stroke="none" font-family="Lato">24</text></svg>
    <h4>24/7 support</h4>
    <p>We offers logistic management services and supply chain perspiciatis unde omnis iste natus error sit voluptat.</p>
  </div>
  <div class="abs feature" style="top:261px">
    <svg width="44" height="44" fill="none" stroke="#ec1f27" stroke-width="1.6"><path d="M4 18L22 6l18 12v22H4z"/><rect x="12" y="22" width="20" height="18"/><path d="M12 28h20M12 34h20"/></svg>
    <h4>10 000m2 Storage Facility</h4>
    <p>We specialize in large items with the facility have 3 15 ton Gantry cranes and heavy mobile lifting equipment we can store items up to 20 ton and we are fully covered and secure. square meter rates from 20m2 to 10,000 m2</p>
  </div>
  <div class="abs feature" style="top:428px">
    <svg width="44" height="44" fill="none" stroke="#ec1f27" stroke-width="1.6"><circle cx="22" cy="22" r="19"/><ellipse cx="22" cy="22" rx="8" ry="19"/><path d="M3 22h38M6 12h32M6 32h32"/></svg>
    <h4>Global service</h4>
    <p>We offers logistic management services and supply chain perspiciatis unde omnis iste natus error sit voluptat.</p>
  </div>
</section>

<div class="abs eyebrow" style="left:128px;top:1326px">Our services</div>
<div class="abs heading" style="left:128px;top:1344px;font-size:27px">What we provide</div>
<div class="abs rule" style="left:128px;top:1399px;width:92px"></div>

<article class="abs svc-card" style="left:128px">
  <div class="photo" role="img" aria-label="Photo of stacked shipping containers at a port" style="background:linear-gradient(180deg,#5f8fc4,#a64a3a 70%,#3b4a5c)"></div>
  <h3>STORAGE</h3>
  <p>SECURE AND SAFE AIR Freight We offers a host of logistic management services and supply chain solutions....</p>
  <div class="btn">Read more</div>
</article>
<article class="abs svc-card" style="left:448px">
  <div class="photo" role="img" aria-label="Photo of a warehouse hall with overhead cranes" style="background:linear-gradient(180deg,#5a6570,#8d9296 60%,#4e5258)"></div>
  <h3>WARE HOUSING</h3>
  <p>SECURE AND SAFE AIR Freight We offers a host of logistic management services and supply chain solutions....</p>
  <div class="btn">Read more</div>
</article>
<article class="abs svc-card" style="left:766px">
  <div class="photo" role="img" aria-label="Photo of a cargo ship at a dock with cranes" style="background:linear-gradient(180deg,#4d5d72,#2f3a4a 60%,#1c2430)"></div>
  <h3>PACKAGING</h3>
  <p>SECURE AND SAFE AIR Freight We offers a host of logistic management services and supply chain solutions....</p>
  <div class="btn">Read more</div>
</article>

<section class="abs about" role="img" aria-label="Dark photo of a container yard">
  <div class="abs about-text" style="top:94px">
    <div style="font-size:12px;font-weight:700">ABOUT US</div>
    <div style="font-size:26px;font-weight:900;margin-top:6px">WE ARE KW</div>
    <p style="font-size:12.5px;line-height:16px;width:340px;margin-top:26px">We offers a host of logistic management services and supply chain solutions. We provide innovative solutions with the best.  Incididunt dolor sit amet, consectetur adipiscing elit, sed dolore magna Incididunt dolor sit amet, consectetur adipiscing elit, sed dolore magna.</p>
    <div style="font-size:17px;font-weight:700;margin-top:78px">OWEN HARTLEY</div>
    <div style="font-size:12px">Founder &amp; CEO</div>
  </div>
</section>
<div class="abs" role="img" aria-label="Photo of an engineer in a hard hat holding a clipboard" style="left:202px;top:1929px;width:352px;height:703px;background:linear-gradient(180deg,#d9b23a 0%,#9fb4d8 20%,#7a8fb8 60%,#8c7a5e 100%)"></div>

<section class="abs testi">
  <div class="abs eyebrow" style="left:85px;top:120px">Testimonial</div>
  <div class="abs heading" style="left:85px;top:136px;font-size:26px">What they say</div>
  <p class="abs body-text" style="left:85px;top:212px;width:300px">They offers a host of logistic management services and supply chain solutions . We provide innovative solutions with the best.  tempor incididunt ut labore et dolor empor tempor incididunt</p>
  <div class="abs" style="left:85px;top:293px;font-size:17px;color:var(--red)">Liam Porter</div>
  <div class="abs body-text" style="left:85px;top:313px">Director, art media</div>
  <div class="abs" role="img" aria-label="Portrait photo of a client" style="left:466px;top:0;width:476px;height:440px;background:linear-gradient(135deg,#f2f2f2,#cfcac0 60%,#a8a296)"></div>
  <div class="abs" style="left:433px;top:163px;width:114px;height:114px;border-radius:50%;background:rgba(236,31,39,.75)"></div>
  <svg class="abs" style="left:463px;top:198px" width="54" height="44" fill="#fff"><path d="M4 2h20v18l-10 22H6l8-20H4zM30 2h20v18L40 42h-8l8-20H30z"/></svg>
</section>

<div class="abs goal" style="top:3062px">
  <svg width="60" height="60" fill="none" stroke="#ec1f27" stroke-width="2"><circle cx="28" cy="32" r="24"/><circle cx="28" cy="32" r="15"/><circle cx="28" cy="32" r="6"/><path d="M28 32L52 8M44 8h8v8"/></svg>
  <h3>Our goals</h3>
  <p>We offers a host of logistic management services and supply chain solutions. consectetur adipiscing elit. Sed ut perspiciatis unde omnis iste natus error sit voluptatem accusantium doloremque laudantium</p>
</div>
<div class="abs goal" style="top:3278px">
  <svg width="60" height="60" fill="none" stroke="#ec1f27" stroke-width="2"><path d="M50 22a24 24 0 1 1-8-12"/><path d="M18 30l10 10 26-28"/></svg>
  <h3>Our vision</h3>
  <p>We offers a host of logistic management services and supply chain solutions. consectetur adipiscing elit. Sed ut perspiciatis unde omnis iste natus error sit voluptatem accusantium doloremque laudantium</p>
</div>

<div class="abs eyebrow" style="left:687px;top:3082px;font-size:13px;text-transform:none">FAQs</div>
<div class="abs heading" style="left:687px;top:3120px;font-size:33px;line-height:40px">Frequently asked<br>questions</div>
<div class="abs rule" style="left:687px;top:3216px;width:64px;background:#2f5b6b"></div>
<div class="abs faq" style="top:3282px">Why choose this?<svg width="16" height="16" stroke="#fff"><path d="M8 0v16M0 8h16"/></svg></div>
<div class="abs faq" style="top:3351px">Is it a Costly<svg width="16" height="16" stroke="#fff"><path d="M8 0v16M0 8h16"/></svg></div>
<div class="abs faq" style="top:3419px">When usally Product Reach<svg width="16" height="16" stroke="#fff"><path d="M8 0v16M0 8h16"/></svg></div>

<section class="abs quote-band" role="img" aria-label="Dark photo of stacked shipping containers"></section>
<section class="abs quote-box">
  <div class="abs" style="left:80px;top:40px;font-size:12px;color:#fff">QUOTE</div>
  <div class="abs" style="left:80px;top:62px;font-size:18px;font-weight:900;color:#fff">REQUEST A FREE QUOTE</div>
  <div class="abs" style="left:80px;top:108px;width:114px;height:2px;background:#fff"></div>
  <div class="field" style="left:80px;top:151px">Your name</div>
  <div class="field" style="left:282px;top:151px">Select a Flight</div>
  <div class="field" style="left:80px;top:221px">Email</div>
  <div class="field" style="left:282px;top:221px">Phone</div>
  <div class="btn" style="left:80px;top:290px;width:113px;height:42px;font-size:11px">Submit</div>
</section>

<footer class="abs footer">
  <div class="abs" style="left:128px;top:120px;display:flex;align-items:center;gap:10px"><i style="width:20px;height:20px;border-radius:50%;background:#fff;display:block"></i><b style="font-size:26px;font-weight:900">KW DEPOT</b></div>
  <p class="abs" style="left:128px;top:229px;width:320px;font-size:12.5px;line-height:15px">We specialize in large items with the facility have 3 15 ton Gantry cranes and heavy mobile lifting equipment we can store items up to 20 ton and we are fully covered and secure. square meter rates from 20m2 to 10,000 m2</p>
  <h5 style="left:527px">Useful links</h5>
  <ul style="left:530px"><li>HOME</li><li>ABOUT US</li><li>SERVICE</li><li>BLOG</li><li>CONTACT</li></ul>
  <h5 style="left:701px">Services</h5>
  <ul style="left:704px"><li>Air Freight</li><li>OCEAN Freight</li><li>WAREHOUSING</li><li>STORAGE</li><li>ROAD Freight</li></ul>
  <h5 style="left:854px">Contact us</h5>
  <div class="abs" style="left:854px;top:160px;font-size:13px;line-height:15px">
    <div style="display:flex;gap:8px"><svg width="12" height="14" fill="none" stroke="#fff"><path d="M6 13C2 8 1 6 1 5a5 5 0 0 1 10 0c0 1-1 3-5 8z"/><circle cx="6" cy="5" r="2"/></svg><span style="width:200px">28 harbour lane 12 district, eastgate port</span></div>
    <div style="display:flex;gap:8px;margin-top:10px"><svg width="12" height="12" fill="none" stroke="#fff"><path d="M3 1l3 3-2 2c1 2 2 3 4 4l2-2 3 3-2 2C5 12 0 7 0 3z"/></svg>0064 219486375</div>
    <div style="display:flex;gap:8px;margin-top:22px"><svg width="12" height="12" fill="none" stroke="#fff"><rect x="1" y="3" width="10" height="7"/><path d="M1 3l5 4 5-4"/></svg>mark@kwdepot.co.nz</div>
  </div>
</footer>

</body>
</html>
```